The Brightwell Clinic :

At The Brightwell Clinic our goal is to provide the most skilled and advanced examination and treatment of the upper neck for superior long-term outcomes for those experiencing headache or migraine.

If a spinal disorder is responsible for the headache and migraine condition the disorder will involve one or more of the top three spinal segments. The fundamental and most powerful feature of The Brightwell Clinic is our method of examining the movements of the top three spinal segments.

We would like the design should communicate professionalism and specialisation.
Updates

Don't necessarily have to have the photos provided.Photo was used for promotional material. I dont have a logo as yet what I  would also like designed.

Project Deadline Extended
Reason: Opening has been delayed due to construction issues of building.

Industry/Entity Type

Clinic

Contact Information for Business Card

The Brightwell Clinic
Suite 3, Oakvale Heath Centre
87 Ferncliff Drive, Kestrel Point NSW 2439
Tel : 63 71 2946 www.thebrightwellclinic.com.au

Requirements
Must have
• Mr Carl Pettigrew
Senior Physiotherapist / Senior Accredited Exercise Physiologist
Ba. App. Sc. (Physiotherapy), Ba Sp. Sc. (Exercise Science), Dip. R.M, MAPA, MESSA, MSMA, MACSM.

Appointment area on back of card

```html
<!DOCTYPE html>
<html lang="en">
<head>
<meta charset="utf-8">
<title>The Brightwell Clinic – Business Cards</title>
<link href="https://fonts.googleapis.com/css2?family=Questrial&display=swap" rel="stylesheet">
<style>
  :root {
    --backdrop: #4a4a4a;
    --card: #ffffff;
    --purple: #5e2a84;
    --green: #8cc63f;
    --grey: #7a7a7a;
    --grey-dark: #666666;
    --photo-light: #f6f1ec;
    --photo-mid: #efe4d8;
    --photo-warm: #e8d7c4;
  }
  * { box-sizing: border-box; margin: 0; padding: 0; }
  html, body { width: 1200px; height: 900px; overflow: hidden; }
  body {
    background: var(--backdrop);
    font-family: "Questrial", "Century Gothic", sans-serif;
    position: relative;
  }
  .card {
    position: absolute;
    top: 300px;
    width: 525px;
    height: 300px;
    background: var(--card);
    overflow: hidden;
    box-shadow: 0 2px 6px rgba(0,0,0,0.35);
  }
  .card--first { left: 58px; }
  .card--second { left: 617px; }
  .card__photo {
    position: absolute;
    top: 0; right: 0;
    width: 290px; height: 300px;
    background:
      radial-gradient(ellipse 45% 55% at 62% 40%, var(--photo-warm) 0%, var(--photo-mid) 45%, transparent 75%),
      linear-gradient(90deg, rgba(255,255,255,1) 0%, var(--photo-light) 35%, var(--photo-mid) 100%);
  }
  .brand {
    position: absolute;
    top: 32px; left: 32px;
    display: flex;
    align-items: center;
  }
  .brand__mark {
    width: 66px; height: 66px;
    border-radius: 50%;
    border: 3px solid var(--purple);
  }
  .brand__rule {
    width: 1px; height: 34px;
    background: var(--grey);
    margin: 0 11px 0 11px;
  }
  .brand__name {
    font-size: 23px;
    color: var(--purple);
    letter-spacing: -0.3px;
    line-height: 1;
  }
  .brand__tagline {
    font-size: 11px;
    color: var(--green);
    margin-top: 3px;
  }
  .person {
    position: absolute;
    top: 120px; left: 32px;
    width: 320px;
  }
  .person__name {
    font-size: 15px;
    color: var(--purple);
    margin-bottom: 4px;
  }
  .person__line {
    font-size: 9.3px;
    color: var(--grey);
    line-height: 14.5px;
  }
  .contact {
    position: absolute;
    top: 212px; left: 32px;
  }
  .contact__clinic {
    font-size: 14px;
    color: var(--purple);
    margin-bottom: 2px;
  }
  .contact__line {
    font-size: 11.5px;
    color: var(--grey-dark);
    line-height: 16px;
  }
  .contact__line--tel { margin-top: 3px; }
  .contact__label { color: var(--purple); }
</style>
</head>
<body>

<section class="card card--first">
  <div class="card__photo" role="img" aria-label="Soft, faded photograph of a woman holding her temples"></div>
  <div class="brand">
    <div class="brand__mark"></div>
    <div class="brand__rule"></div>
    <div>
      <div class="brand__name">Brightwell Clinic</div>
      <div class="brand__tagline">clear thinking, calm living</div>
    </div>
  </div>
  <div class="person">
    <div class="person__name">Mr Owen Hartley</div>
    <div class="person__line">Senior Physiotherapist / Senior Accredited Exercise Physiologist</div>
    <div class="person__line">Practice Director</div>
    <div class="person__line">Master Enrolled. Ba Phty. Ba App Sc HB (APAM, ESSAM)</div>
  </div>
  <div class="contact">
    <div class="contact__clinic">The Brightwell Clinic</div>
    <div class="contact__line">Suite 3, Oakvale Heath Centre</div>
    <div class="contact__line">87 Ferncliff Drive, Kestrel Point NSW 2439</div>
    <div class="contact__line contact__line--tel"><span class="contact__label">tel:</span> 63 71 2946&nbsp; <span class="contact__label">web:</span> www.thebrightwellclinic.com.au</div>
  </div>
</section>

<section class="card card--second">
  <div class="card__photo" role="img" aria-label="Soft, faded photograph of a woman holding her temples"></div>
  <div class="brand">
    <div class="brand__mark"></div>
    <div class="brand__rule"></div>
    <div>
      <div class="brand__name">Brightwell Clinic</div>
      <div class="brand__tagline">clear thinking, calm living</div>
    </div>
  </div>
  <div class="person">
    <div class="person__name">Mr Carl Pettigrew</div>
    <div class="person__line">Senior Physiotherapist / Senior Accredited Exercise Physiologist</div>
    <div class="person__line">Practice Director</div>
    <div class="person__line">Ba. App. Sc. (Physiotherapy), Ba Sp. Sc. (Exercise Science),</div>
    <div class="person__line">Dip. RM, APAM, ESSAM, MSMA, MACSM)</div>
  </div>
  <div class="contact">
    <div class="contact__clinic">The Brightwell Clinic</div>
    <div class="contact__line">Suite 3, Oakvale Heath Centre</div>
    <div class="contact__line">87 Ferncliff Drive, Kestrel Point NSW 2439</div>
    <div class="contact__line contact__line--tel"><span class="contact__label">tel:</span> 63 71 2946&nbsp; <span class="contact__label">web:</span> www.thebrightwellclinic.com.au</div>
  </div>
</section>

</body>
</html>
```